Business Card Design Project

This is the first time we use our new logo. We need a business card that we can use both on our institutional corporate relationships and also that works for our staff that deals with consumers directly.

VELUNDA is a new company dedicated to empower consumers and to provide them with the best choices for specialized health care using the latest telemedicine technology (medicine at a distance via videoconference).

We want to print this cards in high quality materials and process. We will like designs that allow us to use UV spot varnish and other techniques that will differentiate us.

We are including Two different versions of Color logos. In addition we are including white over black background logos. Those can be used replacing the black for a color.

Please note this is the first time we will be creating any corporate materials with our new logo and colors.

Target Market(s)

34+ consumers of medium high and high socioeconomic levels.

Industry/Entity Type

Health

Requirements
Must have
• Our logo on its original colors
Should not have
• Any other graphical element or design that is not our logo

```html
<!DOCTYPE html>
<html lang="en">
<head>
<meta charset="utf-8">
<title>VELUNDA Business Card</title>
<link rel="stylesheet" href="https://fonts.googleapis.com/css2?family=Open+Sans:wght@400;600;700&display=swap">
<style>
  :root {
    --stage: #e4e4e4;
    --card: #ffffff;
    --brand-navy: #1c4f77;
    --brand-teal: #17a69a;
    --text-dark: #444444;
    --text-blue: #1a5a9a;
  }
  * { margin: 0; padding: 0; box-sizing: border-box; }
  html, body {
    width: 1200px;
    height: 1164px;
    overflow: hidden;
    background: var(--stage);
    font-family: "Open Sans", Arial, sans-serif;
  }
  .canvas { position: relative; width: 1200px; height: 1164px; }
  .card {
    position: absolute;
    top: 108px;
    width: 421px;
    height: 736px;
    background: var(--card);
    box-shadow: 0 2px 8px rgba(0,0,0,0.15);
  }
  .card--front { left: 163px; }
  .card--back { left: 615px; }

  .front-brand {
    position: absolute;
    left: 0; right: 0;
    top: 250px;
    text-align: center;
  }
  .brand-dot {
    display: block;
    margin: 0 auto;
    border-radius: 50%;
    background: var(--brand-teal);
  }
  .front-brand .brand-dot { width: 110px; height: 110px; }
  .front-brand .brand-name {
    margin-top: 36px;
    font-size: 58px;
    font-weight: 700;
    letter-spacing: 2px;
    color: var(--brand-navy);
  }

  .back-brand {
    position: absolute;
    left: 0; right: 0;
    top: 70px;
    text-align: center;
  }
  .back-brand .brand-dot { width: 80px; height: 80px; }
  .back-brand .brand-name {
    margin-top: 48px;
    font-size: 52px;
    line-height: 1;
    font-weight: 700;
    letter-spacing: 2px;
    color: var(--brand-navy);
  }

  .holder { position: absolute; left: 48px; top: 338px; }
  .holder-name { font-size: 20px; font-weight: 700; color: var(--text-dark); }
  .holder-role { margin-top: 4px; font-size: 14px; color: var(--text-blue); }

  .contact-list {
    position: absolute;
    left: 44px;
    top: 450px;
    list-style: none;
    font-size: 18px;
    line-height: 24.5px;
    color: var(--text-dark);
  }
  .address {
    position: absolute;
    left: 40px;
    top: 578px;
    width: 360px;
    font-size: 17px;
    line-height: 25px;
    font-style: normal;
    color: var(--text-dark);
  }
</style>
</head>
<body>
<div class="canvas">
  <section class="card card--front" aria-label="Card front">
    <div class="front-brand">
      <span class="brand-dot"></span>
      <div class="brand-name">VELUNDA</div>
    </div>
  </section>

  <section class="card card--back" aria-label="Card back">
    <div class="back-brand">
      <span class="brand-dot"></span>
      <div class="brand-name">VELUNDA</div>
    </div>

    <div class="holder">
      <div class="holder-name">Maren Tolliver</div>
      <div class="holder-role">CEO</div>
    </div>

    <ul class="contact-list">
      <li>P: (000) 000-0000</li>
      <li>F: (000) 000-0000</li>
      <li>E: hello@velunda-care.com</li>
      <li>W: www.velunda-care.com</li>
    </ul>

    <address class="address">
      0000 Larkspur Ave. Suite 000 Fernhollow,<br>
      TT 00000, 000 Larkspur Ave. Suite 000<br>
      Fernhollow, NJ 000000
    </address>
  </section>
</div>
</body>
</html>
```